velunique hair oil

Its an ayurvedic hair oil of 100 ml bottle. We need a design for the label. along with the wordings, some punch line too in the label. Mettalic silver bottle with black cap. Round bottle with height of 10 cm and width of 7 cm. The metallic silver colour bottle can be changed if some other nice colour combination is worked out

Target Market(s)

Retail, any one with a hair fall problem can be our target customer.. This ayurvedic hair oil is a miracle off sorts. With just one bottle hair fall totally stops and fresh hair grows.

Industry/Entity Type

Hair

Requirements
Must have
• HAVE WORDS 100% AYURVEDIC HAIR OIL IN A CIRCLE

MUST NOTE THAT THE BOTTLE IS ROUND
Nice to have
• Its for both men and women. Bottle is round in shape and hence the wording should be accordingly put
Should not have
• RED COLOUR.

```html
<!DOCTYPE html>
<html lang="en">
<head>
<meta charset="utf-8">
<title>velunique hair oil label</title>
<link rel="stylesheet" href="https://fonts.googleapis.com/css2?family=Montserrat:wght@300;400;600;700&display=swap">
<style>
  :root {
    --backdrop: #1c1c1c;
    --hair-dark: #2a120a;
    --hair-mid: #6e2e16;
    --hair-light: #b0582c;
    --badge-green: #1fc24a;
    --ink-black: #111111;
    --label-white: #ffffff;
  }
  html, body {
    margin: 0;
    padding: 0;
    width: 1200px;
    height: 1012px;
    overflow: hidden;
    background: var(--backdrop);
  }
  .canvas {
    position: relative;
    width: 1200px;
    height: 1012px;
    background: var(--backdrop);
  }
  .label {
    position: absolute;
    left: 408px;
    top: 56px;
    width: 384px;
    height: 900px;
    overflow: hidden;
    font-family: "Montserrat", Arial, sans-serif;
    color: var(--label-white);
  }
  .label-hair {
    position: absolute;
    inset: 0;
    background:
      radial-gradient(ellipse 60% 30% at 30% 20%, rgba(176,88,44,0.75), transparent 70%),
      radial-gradient(ellipse 70% 25% at 70% 55%, rgba(176,88,44,0.6), transparent 70%),
      radial-gradient(ellipse 60% 30% at 35% 85%, rgba(150,70,34,0.7), transparent 70%),
      linear-gradient(160deg, var(--hair-mid) 0%, var(--hair-dark) 35%, var(--hair-mid) 60%, var(--hair-dark) 100%);
  }
  .brand-name {
    position: absolute;
    top: 92px;
    left: 0;
    right: 0;
    text-align: center;
    font-weight: 400;
    font-size: 44px;
    letter-spacing: 0.5px;
  }
  .claim-badge {
    position: absolute;
    left: 12px;
    top: 208px;
    width: 360px;
    height: 360px;
    border-radius: 50%;
    background: var(--badge-green);
    color: var(--ink-black);
    text-align: center;
    font-weight: 700;
  }
  .claim-percent {
    position: absolute;
    top: 98px;
    left: 0;
    right: 0;
    font-size: 72px;
    line-height: 1;
    font-weight: 600;
  }
  .claim-words {
    position: absolute;
    top: 180px;
    left: 0;
    right: 0;
    font-size: 40px;
    line-height: 1.05;
    font-weight: 700;
  }
  .audience {
    position: absolute;
    top: 596px;
    left: 0;
    right: 0;
    text-align: center;
    font-size: 40px;
    font-weight: 300;
  }
  .ingredient {
    position: absolute;
    top: 690px;
    left: 0;
    right: 0;
    text-align: center;
    font-size: 26px;
    line-height: 1.05;
    font-weight: 400;
  }
  .volume {
    position: absolute;
    top: 790px;
    left: 0;
    right: 0;
    text-align: center;
    font-size: 26px;
    font-weight: 400;
  }
</style>
</head>
<body>
<div class="canvas">
  <div class="label">
    <div class="label-hair" role="img" aria-label="Close-up photograph of glossy wavy auburn hair"></div>
    <div class="brand-name">velunique</div>
    <div class="claim-badge">
      <div class="claim-percent">100%</div>
      <div class="claim-words">AYURVEDIC<br>HAIR OIL</div>
    </div>
    <div class="audience">UNISEX</div>
    <div class="ingredient">VIRGIN<br>COCONUT OIL</div>
    <div class="volume">100ml</div>
  </div>
</div>
</body>
</html>
```